Vantrel

I already have a website created through Plovix.com - https://vantrel.co.nz.

Its an accounting services business, can get ideas from tzhl.co.nz, fwu.co.nz, yrx.co.nz

I would like to have this recreated using coding. I need the following features and functionalities incorporated:

- Live Chat feature
- Moving Carousel feature for Reviews
- Advanced SEO support (Google Analytics)

Industry/Entity Type

accounting

Coding

Coded - Design and coding required

Number of Pages Required

5+ page

```html
<!DOCTYPE html>
<html lang="en">
<head>
<meta charset="utf-8">
<title>Vantrel — Accounting Services</title>
<link href="https://fonts.googleapis.com/css2?family=Poppins:ital,wght@0,400;0,500;0,600;0,700;1,400&display=swap" rel="stylesheet">
<style>
:root{
  --dark:#3c4b48;
  --dark-2:#34423f;
  --mint:#a3d9cb;
  --mint-text:#8ccfbe;
  --olive:#2f3d2c;
  --ink:#333b3a;
  --muted:#5b6462;
  --white:#ffffff;
  --star:#f2b632;
}
*{box-sizing:border-box;margin:0;padding:0}
html,body{width:1200px;height:5008px;overflow:hidden}
body{position:relative;background:var(--white);font-family:'Poppins',sans-serif;color:var(--ink)}
.abs{position:absolute}
.photo{position:absolute;background:linear-gradient(135deg,#9aa9a6,#5f6f6c)}
/* header / hero */
.hero{left:0;top:0;width:1200px;height:681px;background:var(--dark)}
.brand{left:126px;top:40px;display:flex;align-items:center;gap:12px;color:var(--white);font-weight:600;font-size:30px;letter-spacing:5px}
.brand-dot{width:44px;height:44px;border-radius:50%;background:var(--mint)}
.nav{top:48px;color:var(--white);font-size:13px;font-weight:500;text-transform:uppercase}
.nav-cta{left:934px;top:39px;width:138px;height:43px;border-radius:22px;background:var(--mint);color:var(--white);font-size:12px;font-weight:500;display:flex;align-items:center;justify-content:center}
.hero-title{left:122px;top:244px;width:400px;color:var(--white);font-size:40px;line-height:47px;font-weight:700}
.btn{left:122px;top:455px;width:144px;height:43px;border-radius:22px;background:var(--mint);color:var(--dark);font-size:16px;font-weight:600;display:flex;align-items:center;justify-content:center}
.hero-photo{left:428px;top:165px;width:772px;height:516px;background:linear-gradient(160deg,#6f8581,#47524f)}
/* features */
.feature{top:753px;width:302px;height:83px;background:var(--white);border-radius:8px;box-shadow:0 4px 18px rgba(0,0,0,.12);display:flex;align-items:center;gap:16px;padding-left:20px;font-size:20px;line-height:24px;font-weight:500;color:var(--ink)}
.feature-icon{width:44px;height:44px;border-radius:50%;border:3px solid var(--mint);flex:none}
/* welcome */
.section-title{left:0;width:1200px;text-align:center;font-size:34px;font-weight:700;color:var(--ink)}
.welcome-text{left:236px;top:996px;width:728px;text-align:center;font-size:16.5px;line-height:24.5px;color:var(--muted)}
.welcome-photo{left:216px;top:1134px;width:767px;height:348px;border-radius:22px;background:linear-gradient(135deg,#8a6a4d,#3e4a52)}
/* services */
.service{top:1698px;width:281px;height:434px;background:var(--white);box-shadow:0 4px 16px rgba(0,0,0,.12);overflow:hidden}
.service.is-active{background:var(--dark);color:var(--white)}
.service-img{height:202px;background:linear-gradient(135deg,#4d6c8a,#23364a)}
.service-title{position:absolute;left:27px;top:232px;font-size:19px;line-height:24px;font-weight:600}
.service-text{position:absolute;left:27px;top:298px;width:230px;font-size:14px;line-height:19.5px;color:var(--muted)}
.is-active .service-text{color:#e6ecea}
.service-arrow{position:absolute;left:227px;top:384px;width:28px;height:28px}
/* proud */
.proud-title{left:126px;top:2363px;font-size:32px;line-height:38px;font-weight:700;color:var(--olive)}
.proud-text{left:126px;top:2467px;width:404px;font-size:14.6px;line-height:22.4px;color:var(--muted)}
.proud-photo{left:585px;top:2250px;width:615px;height:525px;border-radius:26px 0 0 26px;background:linear-gradient(135deg,#7e9f8c,#496a80)}
.proud-strip{left:1140px;top:2760px;width:60px;height:15px;background:var(--mint)}
/* reviews */
.reviews{left:0;top:2898px;width:1200px;height:498px;background:var(--dark)}
.reviews-title{left:0;top:2962px;width:1200px;text-align:center;color:var(--white);font-size:31px;font-weight:600}
.review{top:3044px;width:247px;height:259px;background:var(--white);border-radius:8px;padding:28px 18px}
.review-head{display:flex;align-items:center;gap:10px}
.avatar{width:46px;height:46px;border-radius:50%;background:linear-gradient(135deg,#9aa7b3,#4b5866)}
.review-name{font-size:14px;font-weight:700;color:var(--ink)}
.stars{color:var(--star);font-size:11px;letter-spacing:1px}
.review-text{margin-top:12px;font-size:14.5px;line-height:21.5px;font-style:italic;color:var(--muted)}
.carousel-btn{top:3138px;width:38px;height:38px}
/* includes */
.inc-photo{border-radius:12px}
.inc-title{left:591px;top:3520px;width:500px;font-size:33px;line-height:39px;font-weight:600;color:var(--mint-text)}
.inc-text{left:591px;width:480px;font-size:14.6px;line-height:21.5px;color:var(--muted)}
/* insights */
.insights{left:68px;top:4061px;width:1064px;height:516px;border-radius:30px;background:var(--dark)}
.insights-title{left:0;top:4105px;width:1200px;text-align:center;color:var(--white);font-size:32px;font-weight:700}
.insight-img{top:4190px;width:284px;height:212px;background:linear-gradient(135deg,#b8a78f,#4f5d6a)}
.insight-title{top:4420px;width:284px;color:var(--white);font-size:19px;line-height:24px;font-weight:600}
.insight-date{top:4492px;color:var(--mint);font-size:11px;font-weight:600}
/* footer */
.footer{left:0;top:4668px;width:1200px;height:340px;background:var(--dark)}
.footer-brand{left:120px;top:4853px;color:var(--mint);font-size:30px;font-weight:600;letter-spacing:6px}
.footer-mark{left:174px;top:4748px;width:78px;height:78px;border-radius:50%;border:8px solid var(--mint)}
.footer-nav{left:412px;top:4745px;color:var(--white);font-size:14px;font-weight:500;line-height:31px}
.contact-ico{width:40px;height:40px;border-radius:50%;background:var(--mint);display:flex;align-items:center;justify-content:center}
.contact-text{color:var(--white);font-size:14px;line-height:21px;font-weight:500}
.social{top:4782px;width:42px;height:42px;border-radius:50%;border:2px solid var(--mint)}
.copyright{left:0;top:4945px;width:1200px;text-align:center;color:var(--white);font-size:14px}
</style>
</head>
<body>

<!-- Hero -->
<section class="abs hero"></section>
<div class="abs brand"><span class="brand-dot"></span>VANTREL</div>
<nav>
  <a class="abs nav" style="left:512px">Home</a>
  <a class="abs nav" style="left:605px">Services</a>
  <a class="abs nav" style="left:725px">About Us</a>
  <a class="abs nav" style="left:847px">Pricing</a>
  <a class="abs nav-cta">CONTACT US</a>
</nav>
<div class="abs hero-photo" role="img" aria-label="Three accountants reviewing documents together at a laptop"></div>
<h1 class="abs hero-title">We Empower Businesses Ledgra Certified, Results Driven</h1>
<a class="abs btn">CONTACT</a>

<!-- Features -->
<div class="abs feature" style="left:88px"><span class="feature-icon"></span>Tailored<br>Financial Solutions</div>
<div class="abs feature" style="left:449px"><span class="feature-icon"></span>Ledgra Advisor<br>Certified</div>
<div class="abs feature" style="left:809px"><span class="feature-icon"></span>Enhanced<br>Financial Clarity</div>

<!-- Welcome -->
<h2 class="abs section-title" style="top:920px">WELCOME TO VANTREL</h2>
<p class="abs welcome-text">We pride ourselves on offering premium yet affordable accounting services to a wide range of organizations, with a focus on Crown Funded organisations supported by the Health Directorate, Social Support Directorate &amp; Learning Directorate that deliver essential community-based services and programmes.</p>
<div class="abs welcome-photo" role="img" aria-label="Team working over financial charts and a laptop on a wooden desk"></div>

<!-- Services -->
<h2 class="abs section-title" style="top:1605px">OUR SERVICES</h2>
<article class="abs service is-active" style="left:126px">
  <div class="service-img" role="img" aria-label="Hands pointing at printed financial charts"></div>
  <h3 class="service-title">Monthly<br>Reporting</h3>
  <p class="service-text">Lorem ipsum dolor sit ametlo con sectetur adipiscing elitse oeiusmod tempor incididunt ut labore et dolore.</p>
  <svg class="service-arrow" viewBox="0 0 28 28"><circle cx="14" cy="14" r="12.5" fill="none" stroke="#a3d9cb" stroke-width="1.5"/><path d="M12 9l5 5-5 5" fill="none" stroke="#a3d9cb" stroke-width="1.5"/></svg>
</article>
<article class="abs service" style="left:445px">
  <div class="service-img" role="img" aria-label="Presenter explaining charts on a screen to a colleague"></div>
  <h3 class="service-title">Financial Performance<br>&amp; Analysis</h3>
  <p class="service-text">Lorem ipsum dolor sit ametlo con sectetur adipiscing elitse oeiusmod tempor incididunt ut labore et dolore.</p>
  <svg class="service-arrow" viewBox="0 0 28 28"><circle cx="14" cy="14" r="12.5" fill="none" stroke="#a3d9cb" stroke-width="1.5"/><path d="M12 9l5 5-5 5" fill="none" stroke="#a3d9cb" stroke-width="1.5"/></svg>
</article>
<article class="abs service" style="left:764px">
  <div class="service-img" role="img" aria-label="Hands using a tablet showing cash flow charts"></div>
  <h3 class="service-title">Cash Flow<br>Reporting</h3>
  <p class="service-text">Lorem ipsum dolor sit ametlo con sectetur adipiscing elitse oeiusmod tempor incididunt ut labore et dolore.</p>
  <svg class="service-arrow" viewBox="0 0 28 28"><circle cx="14" cy="14" r="12.5" fill="none" stroke="#a3d9cb" stroke-width="1.5"/><path d="M12 9l5 5-5 5" fill="none" stroke="#a3d9cb" stroke-width="1.5"/></svg>
</article>
<article class="abs service" style="left:1082px">
  <div class="service-img" role="img" aria-label="Laptop displaying annual statement figures"></div>
  <h3 class="service-title" style="white-space:nowrap">Annual Financial<br>Statements</h3>
  <p class="service-text">Lorem ipsum dolor sit ametlo con sectetur adipiscing elitse oeiusmod tempor incididunt ut labore et dolore.</p>
</article>

<!-- Certified -->
<h2 class="abs proud-title">We are proud to be<br>Ledgra Advisor Certified</h2>
<p class="abs proud-text">Providing cloud-based accounting solutions that streamline your financial processes while ensuring accuracy and compliance. Whether you're looking for help with financial reporting, budgeting, grant management, or tax filings, our dedicated team is here to support your growth and success. We're committed to helping you navigate the complexities of accounting, allowing you to focus on what truly matters—achieving your mission and objectives.</p>
<div class="abs proud-photo" role="img" aria-label="Accountant reading a document beside a laptop near a window"></div>
<div class="abs proud-strip"></div>

<!-- Reviews -->
<section class="abs reviews"></section>
<h2 class="abs reviews-title">Latest Reviews</h2>
<svg class="abs carousel-btn" style="left:16px" viewBox="0 0 38 38"><circle cx="19" cy="19" r="17" fill="none" stroke="#fff" stroke-width="1.5"/><path d="M21 13l-6 6 6 6" fill="none" stroke="#fff" stroke-width="1.5"/></svg>
<svg class="abs carousel-btn" style="left:1150px" viewBox="0 0 38 38"><circle cx="19" cy="19" r="17" fill="none" stroke="#fff" stroke-width="1.5"/><path d="M17 13l6 6-6 6" fill="none" stroke="#fff" stroke-width="1.5"/></svg>
<div class="abs review" style="left:74px"><div class="review-head"><div class="avatar" role="img" aria-label="Reviewer portrait"></div><div><div class="review-name">ARIA KENT</div><div class="stars">★★★★★</div></div></div><p class="review-text">Lorem ipsum lorlosiam lore con sectetur adip iscing elit sed do eiusmodtem por inc ididunt ut labore etdoore magna aluauis ipsum suspe ndis.</p></div>
<div class="abs review" style="left:344px"><div class="review-head"><div class="avatar" role="img" aria-label="Reviewer portrait"></div><div><div class="review-name">ARIA KENT</div><div class="stars">★★★★★</div></div></div><p class="review-text">Lorem ipsum lorlosiam lore con sectetur adip iscing elit sed do eiusmodtem por inc ididunt ut labore etdoore magna aluauis ipsum suspe ndis.</p></div>
<div class="abs review" style="left:615px"><div class="review-head"><div class="avatar" role="img" aria-label="Reviewer portrait"></div><div><div class="review-name">ARIA KENT</div><div class="stars">★★★★★</div></div></div><p class="review-text">Lorem ipsum lorlosiam lore con sectetur adip iscing elit sed do eiusmodtem por inc ididunt ut labore etdoore magna aluauis ipsum suspe ndis.</p></div>
<div class="abs review" style="left:885px"><div class="review-head"><div class="avatar" role="img" aria-label="Reviewer portrait"></div><div><div class="review-name">ARIA KENT</div><div class="stars">★★★★★</div></div></div><p class="review-text">Lorem ipsum lorlosiam lore con sectetur adip iscing elit sed do eiusmodtem por inc ididunt ut labore etdoore magna aluauis ipsum suspe ndis.</p></div>

<!-- Organisations -->
<div class="photo inc-photo" style="left:126px;top:3530px;width:148px;height:171px;background:linear-gradient(135deg,#d6b59a,#4a3a33)" role="img" aria-label="Caregiver holding an elderly person's hands"></div>
<div class="photo inc-photo" style="left:300px;top:3493px;width:219px;height:216px;background:linear-gradient(135deg,#c9a27c,#5d7b8c)" role="img" aria-label="Two women smiling while working at a laptop"></div>
<div class="photo inc-photo" style="left:113px;top:3733px;width:202px;height:204px;background:linear-gradient(135deg,#e5e8ea,#8e98a0)" role="img" aria-label="Laptop showing financial charts beside a hand holding a pen"></div>
<div class="photo inc-photo" style="left:350px;top:3733px;width:195px;height:206px;background:linear-gradient(135deg,#c9c8bd,#4f5c55)" role="img" aria-label="Man working on a tablet at a desk with plants"></div>
<h2 class="abs inc-title">This includes organisations operating under government contracts to provide services such as</h2>
<p class="abs inc-text" style="top:3706px">Mental Health Support, Residential Disability Care, Youth Development, Family and Social Services and other wellbeing initiatives. We also work with Charitable Trusts and Schools providing tailored support to meet their specific financial and compliance requirements.</p>
<p class="abs inc-text" style="top:3833px">As Chartered Accountants we bring extensive expertise and a personalised approach to help your organisation navigate its financial responsibilities with confidence.</p>

<!-- Insights -->
<section class="abs insights"></section>
<h2 class="abs insights-title">LATEST INSIGHTS</h2>
<div class="abs insight-img" style="left:122px" role="img" aria-label="Laptop and coffee cup on a desk with reports"></div>
<div class="abs insight-img" style="left:455px" role="img" aria-label="Team gathered around a table of documents, seen from above"></div>
<div class="abs insight-img" style="left:788px" role="img" aria-label="Two colleagues reviewing figures on a monitor"></div>
<h3 class="abs insight-title" style="left:122px">Lorem ipsum dolor sit amet, consectetur</h3>
<h3 class="abs insight-title" style="left:455px">Lorem ipsum dolor sit amet, consectetur</h3>
<h3 class="abs insight-title" style="left:788px">Lorem ipsum dolor sit amet, consectetur</h3>
<span class="abs insight-date" style="left:122px">JUNE 13 2025</span>
<span class="abs insight-date" style="left:455px">JUNE 13 2025</span>
<span class="abs insight-date" style="left:788px">JUNE 13 2025</span>

<!-- Footer -->
<footer>
  <div class="abs footer"></div>
  <div class="abs footer-mark"></div>
  <div class="abs footer-brand">VANTREL</div>
  <ul class="abs footer-nav" style="list-style:none">
    <li>HOME</li><li>SERVICES</li><li>ABOUT US</li><li>PRICING</li><li>CONTACT US</li>
  </ul>
  <div class="abs" style="left:609px;top:4755px;display:flex;gap:12px;align-items:center">
    <span class="contact-ico"><svg width="20" height="16" viewBox="0 0 20 16"><rect x="1" y="1" width="18" height="14" rx="2" fill="none" stroke="#3c4b48" stroke-width="1.6"/><path d="M1.5 2l8.5 7 8.5-7" fill="none" stroke="#3c4b48" stroke-width="1.6"/></svg></span>
    <span class="contact-text">Email:<br>contact@vantrel.co.nz</span>
  </div>
  <div class="abs" style="left:609px;top:4826px;display:flex;gap:12px;align-items:center">
    <span class="contact-ico"><svg width="18" height="18" viewBox="0 0 24 24"><path d="M6.6 10.8a15 15 0 006.6 6.6l2.2-2.2a1 1 0 011-.25 11.4 11.4 0 003.6.57 1 1 0 011 1V20a1 1 0 01-1 1A17 17 0 013 4a1 1 0 011-1h3.5a1 1 0 011 1c0 1.25.2 2.45.57 3.6a1 1 0 01-.25 1z" fill="#3c4b48"/></svg></span>
    <span class="contact-text">Call:<br>021 555 0142</span>
  </div>
  <span class="abs social" style="left:973px"></span>
  <span class="abs social" style="left:1027px"></span>
  <p class="abs copyright">Copyright © 2025 Vantrel. All rights are reserved.</p>
</footer>

</body>
</html>
```